Exceptional Corporate Business Card Design

Hello,

We need an exceptional corporate business card design based on our logo attached. We require:

1. A Variation for letterpress print
2. Standard size of business card 84mm x 55mm (Artwork 88mm x 59mm)
3. Variation for square business card 65mm x 65mm (Artwork 69mm x 69mm)
4. Variation as a one side print
5. Adobe Illustrator files

The company is in the financial industry, dulvant.com

The logo is attached as vector pdf.
regards

```html
<!DOCTYPE html>
<html lang="en">
<head>
<meta charset="utf-8">
<title>Dulvant Business Card</title>
<link href="https://fonts.googleapis.com/css2?family=Cinzel:wght@400;600&display=swap" rel="stylesheet">
<style>
  :root {
    --backdrop: #4a4039;
    --card: #131416;
    --card-edge: #0a0b0c;
    --emboss: #1c1d20;
    --emboss-line: #2a2b2f;
    --silver: #8d8f94;
    --brand-blue: #3b35a8;
    --text-light: #eceae6;
  }
  * { margin: 0; padding: 0; box-sizing: border-box; }
  html, body { width: 1200px; height: 716px; overflow: hidden; }
  body {
    background: var(--backdrop);
    font-family: "Cinzel", Georgia, serif;
    position: relative;
  }
  .card {
    position: absolute;
    top: 195px;
    width: 500px;
    height: 327px;
    background: var(--card);
    box-shadow: 0 14px 30px rgba(0,0,0,.45);
    border: 1px solid var(--card-edge);
    overflow: hidden;
  }
  .card--front { left: 60px; }
  .card--back { left: 640px; }

  .wordmark {
    display: flex;
    align-items: center;
    gap: 12px;
    font-weight: 600;
    letter-spacing: 2px;
  }
  .wordmark__dot { border-radius: 50%; flex: none; }

  .card--front .wordmark {
    position: absolute;
    left: 50%; top: 50%;
    transform: translate(-50%, -50%);
    color: var(--silver);
    font-size: 48px;
  }
  .card--front .wordmark__dot {
    width: 62px; height: 62px;
    border: 3px solid var(--emboss-line);
    background: var(--emboss);
  }

  .back__emblem {
    position: absolute;
    left: -40px; top: 70px;
    width: 190px; height: 190px;
    border-radius: 50%;
    background: var(--emboss);
    border: 4px solid var(--emboss-line);
  }

  .back__info {
    position: absolute;
    right: 34px; top: 40px;
    text-align: right;
    color: var(--text-light);
  }
  .card--back .wordmark {
    justify-content: flex-end;
    color: var(--brand-blue);
    font-size: 38px;
    margin-bottom: 22px;
  }
  .card--back .wordmark__dot {
    width: 48px; height: 48px;
    background: var(--brand-blue);
  }
  .person__name { color: var(--brand-blue); font-size: 17px; font-weight: 600; }
  .person__role { font-size: 13px; margin-bottom: 16px; }
  .address { font-size: 13px; line-height: 1.45; font-style: normal; margin-bottom: 18px; }
  .contacts { list-style: none; font-size: 13px; line-height: 1.5; }
  .contacts li { display: flex; justify-content: flex-end; align-items: center; gap: 8px; }
  .contacts svg { width: 12px; height: 12px; fill: none; stroke: var(--brand-blue); stroke-width: 1.6; }
</style>
</head>
<body>
  <section class="card card--front" aria-label="Card front">
    <div class="wordmark"><span class="wordmark__dot"></span><span>DULVANT</span></div>
  </section>

  <section class="card card--back" aria-label="Card back">
    <div class="back__emblem" role="img" aria-label="Blind-embossed brand emblem decoration"></div>
    <div class="back__info">
      <div class="wordmark"><span class="wordmark__dot"></span><span>DULVANT</span></div>
      <p class="person__name">Marlo Venn</p>
      <p class="person__role">Founder &amp; CEO</p>
      <address class="address">14-16 Larch Row,<br>EC2 7QT, London, England</address>
      <ul class="contacts">
        <li>+43 1 55021847
          <svg viewBox="0 0 12 12"><path d="M2 1.5h2.5l1 2.5-1.5 1a6 6 0 0 0 3 3l1-1.5 2.5 1V10.5A1 1 0 0 1 9.5 11.5 9 9 0 0 1 .5 2.5 1 1 0 0 1 2 1.5z"/></svg></li>
        <li>office@dulvant.com
          <svg viewBox="0 0 12 12"><rect x="1" y="2.5" width="10" height="7"/><path d="M1 2.5l5 4 5-4"/></svg></li>
        <li>www.dulvant.com
          <svg viewBox="0 0 12 12"><circle cx="6" cy="6" r="5"/><path d="M1 6h10M6 1c-2.5 3-2.5 7 0 10M6 1c2.5 3 2.5 7 0 10"/></svg></li>
      </ul>
    </div>
  </section>
</body>
</html>
```